Modern Business Card

Modern professional business card with more than just logo and demographic info. Something memorable.

We are a trendy/modern chiropractic group with an emphasis on neurology, hence the minimalist-type brain logo. We want to convey that modern and technical aspect with professionalism and the elite nature of our practice environment.

```html
<!DOCTYPE html>
<html lang="en">
<head>
<meta charset="utf-8">
<title>Northway Chiropractic – Business Card</title>
<link rel="stylesheet" href="https://fonts.googleapis.com/css2?family=Open+Sans:wght@400;700&display=swap">
<style>
  :root {
    --brand-blue: #4880c1;
    --ink: #111111;
    --ink-soft: #5a5a5a;
    --paper: #ffffff;
    --page: #ffffff;
    --card-shadow: 0 2px 10px rgba(0, 0, 0, 0.12);
  }
  * { box-sizing: border-box; margin: 0; padding: 0; }
  html, body {
    width: 1200px;
    height: 1200px;
    overflow: hidden;
    background: var(--page);
    font-family: "Open Sans", Arial, sans-serif;
  }
  .canvas { position: relative; width: 1200px; height: 1200px; }

  .card {
    position: absolute;
    left: 115px;
    width: 970px;
    height: 554px;
    box-shadow: var(--card-shadow);
  }
  .card--front { top: 42px; background: var(--brand-blue); }
  .card--back { top: 605px; background: var(--paper); }

  /* Front */
  .front-mark {
    position: absolute;
    left: 50%;
    top: 168px;
    width: 110px;
    height: 110px;
    margin-left: -55px;
    border-radius: 50%;
    background: var(--paper);
  }
  .front-name {
    position: absolute;
    left: 0;
    right: 0;
    top: 300px;
    text-align: center;
    color: var(--paper);
    font-weight: 400;
    line-height: 1;
  }
  .front-name .line-main { display: block; font-size: 62px; letter-spacing: 1px; }
  .front-name .line-sub { display: block; font-size: 33px; margin-top: 6px; letter-spacing: 1px; }

  /* Back */
  .brand {
    position: absolute;
    left: 70px;
    top: 78px;
    display: flex;
    align-items: center;
    gap: 14px;
  }
  .brand-dot {
    width: 104px;
    height: 104px;
    border-radius: 50%;
    background: var(--brand-blue);
    flex: none;
  }
  .brand-name {
    color: var(--ink);
    font-weight: 400;
    line-height: 1;
  }
  .brand-name .line-main { display: block; font-size: 50px; letter-spacing: 1px; }
  .brand-name .line-sub { display: block; font-size: 27px; margin-top: 4px; letter-spacing: 1px; }

  .person {
    position: absolute;
    right: 69px;
    top: 72px;
    text-align: right;
  }
  .person-name { font-size: 34px; font-weight: 700; color: #000; line-height: 1.2; }
  .person-role { font-size: 26px; font-weight: 400; color: var(--ink-soft); line-height: 1.3; }

  .address {
    position: absolute;
    left: 68px;
    top: 252px;
    font-size: 25px;
    line-height: 35px;
    color: var(--ink-soft);
  }
  .contacts {
    position: absolute;
    left: 68px;
    top: 372px;
    list-style: none;
    font-size: 25px;
    color: var(--ink-soft);
  }
  .contacts li {
    display: flex;
    align-items: center;
    height: 36px;
  }
  .contacts svg { width: 24px; height: 24px; margin-right: 18px; flex: none; }

  .corner-dot {
    position: absolute;
    left: 697px;
    top: 263px;
    width: 204px;
    height: 204px;
    border-radius: 50%;
    background: var(--brand-blue);
  }
</style>
</head>
<body>
<main class="canvas">

  <section class="card card--front" aria-label="Card front">
    <div class="front-mark"></div>
    <h1 class="front-name">
      <span class="line-main">NORTHWAY</span>
      <span class="line-sub">CHIROPRACTIC</span>
    </h1>
  </section>

  <section class="card card--back" aria-label="Card back">
    <div class="brand">
      <div class="brand-dot"></div>
      <h2 class="brand-name">
        <span class="line-main">NORTHWAY</span>
        <span class="line-sub">CHIROPRACTIC</span>
      </h2>
    </div>

    <div class="person">
      <p class="person-name">Daniel Reyes</p>
      <p class="person-role">President</p>
    </div>

    <p class="address">Street Name Here, Suite 100<br>Street Zip Code,Country</p>

    <ul class="contacts">
      <li>
        <svg viewBox="0 0 24 24" aria-hidden="true"><path fill="#4880c1" d="M6.6 10.8a15.2 15.2 0 0 0 6.6 6.6l2.2-2.2c.3-.3.7-.4 1-.2 1.1.4 2.3.6 3.6.6.6 0 1 .4 1 1V20c0 .6-.4 1-1 1A17 17 0 0 1 3 4c0-.6.4-1 1-1h3.5c.6 0 1 .4 1 1 0 1.3.2 2.5.6 3.6.1.3 0 .7-.2 1z"/></svg>
        01234-56789
      </li>
      <li>
        <svg viewBox="0 0 24 24" aria-hidden="true"><rect x="2" y="5" width="20" height="14" fill="#4880c1"/><path d="M2.5 5.5 12 13l9.5-7.5M2.5 18.5l7-6.5M21.5 18.5l-7-6.5" fill="none" stroke="#fff" stroke-width="1.4"/></svg>
        info@yourwebsite.com
      </li>
      <li>
        <svg viewBox="0 0 24 24" aria-hidden="true"><g fill="none" stroke="#4880c1" stroke-width="1.6"><circle cx="12" cy="12" r="9.5"/><ellipse cx="12" cy="12" rx="4.2" ry="9.5"/><path d="M2.5 12h19M4 7h16M4 17h16M12 2.5v19"/></g></svg>
        www.yourwebsite.com
      </li>
    </ul>

    <div class="corner-dot"></div>
  </section>

</main>
</body>
</html>
```